FURLOW MEADOW Pet Resorts Outdoor Signage

4 x 8 outdoor signage design for our two locations

Target Market(s)

Existing and New Customers

Industry/Entity Type

Pet Care

Font styles to use
Sans Serif

Colors

Designer to choose colors to be used in the design.

```html
<!DOCTYPE html>
<html lang="en">
<head>
<meta charset="utf-8">
<title>FURLOW MEADOW Pet Resort – Outdoor Sign</title>
<link rel="stylesheet" href="https://fonts.googleapis.com/css2?family=Montserrat:wght@700&family=Questrial&display=swap">
<style>
  :root {
    --navy: #0c0c42;
    --gold: #f7b844;
    --white: #ffffff;
    --page: #ffffff;
  }
  * { margin: 0; padding: 0; box-sizing: border-box; }
  html, body {
    width: 1200px; height: 1000px; overflow: hidden;
    background: var(--page);
  }
  .sign {
    position: absolute;
    left: 12px; top: 206px;
    width: 1176px; height: 588px;
    background: var(--navy);
  }
  .brand-name {
    position: absolute;
    left: 58px; top: 150px;
    font-family: "Montserrat", sans-serif;
    font-weight: 700;
    font-size: 76px;
    line-height: 1.1;
    color: var(--gold);
    letter-spacing: 1px;
    white-space: nowrap;
  }
  .offer-title,
  .offer-tagline,
  .service-row,
  .contact {
    position: absolute;
    right: 28px;
    white-space: nowrap;
  }
  .offer-title {
    top: 50px;
    font-family: "Montserrat", sans-serif;
    font-weight: 700;
    font-size: 88px;
    line-height: 1;
    color: var(--white);
    letter-spacing: 0;
  }
  .offer-tagline {
    top: 172px;
    font-family: "Questrial", sans-serif;
    font-size: 52px;
    line-height: 1;
    color: var(--gold);
    letter-spacing: 4px;
  }
  .service-row {
    display: flex;
    align-items: center;
    gap: 12px;
    font-family: "Questrial", sans-serif;
    font-size: 30px;
    line-height: 1;
    color: var(--white);
  }
  .service-row.first { top: 308px; }
  .service-row.second { top: 371px; right: 58px; }
  .bullet { width: 28px; height: 28px; flex: none; }
  .contact {
    top: 496px;
    display: flex;
    align-items: center;
    gap: 12px;
    font-family: "Questrial", sans-serif;
    font-size: 33px;
    line-height: 1;
    color: var(--white);
    letter-spacing: 0.5px;
  }
</style>
</head>
<body>
<svg width="0" height="0" style="position:absolute" aria-hidden="true">
  <defs>
    <symbol id="bone-bullet" viewBox="0 0 28 28">
      <circle cx="14" cy="14" r="14" fill="#f7b844"/>
      <rect x="9" y="12.6" width="10" height="2.8" fill="#0c0c42"/>
      <circle cx="8.6" cy="12.4" r="2" fill="#0c0c42"/>
      <circle cx="8.6" cy="15.6" r="2" fill="#0c0c42"/>
      <circle cx="19.4" cy="12.4" r="2" fill="#0c0c42"/>
      <circle cx="19.4" cy="15.6" r="2" fill="#0c0c42"/>
    </symbol>
  </defs>
</svg>

<main class="sign">
  <div class="brand-name">FURLOW<br>MEADOW</div>

  <h1 class="offer-title">PET RESORT</h1>
  <p class="offer-tagline">ALL BREED FRIENDLY</p>

  <div class="service-row first">
    <svg class="bullet"><use href="#bone-bullet"/></svg><span>BOARDING</span>
    <svg class="bullet"><use href="#bone-bullet"/></svg><span>DAYCARE</span>
    <svg class="bullet"><use href="#bone-bullet"/></svg><span>TRAINING</span>
    <svg class="bullet"><use href="#bone-bullet"/></svg>
  </div>
  <div class="service-row second">
    <svg class="bullet"><use href="#bone-bullet"/></svg><span>GROOMING</span>
    <svg class="bullet"><use href="#bone-bullet"/></svg><span>PET TAXI &amp; MORE</span>
    <svg class="bullet"><use href="#bone-bullet"/></svg>
  </div>

  <div class="contact">
    <span>www.furlowmeadow.ca</span>
    <svg class="bullet"><use href="#bone-bullet"/></svg>
    <span>905-555-0142</span>
  </div>
</main>
</body>
</html>
```